Brightwell Pictures Business Card

Hello,

i would like to have a dynamic, creative but tasteful card, colour used, front and back. I have attached a sample card that I liked very much from another individual to give you an idea of the theme/approach, but not colour. Ideally the graphic elements of the Brightwell Logo are brought into the design.

Target Market(s)

North America

Industry/Entity Type

Film Production

Contact Information for Business Card

Mirela Vantasch
President/Founder
Brightwell Pictures Inc.
587 914 3362
mirela@brightwellpix.tv

Font styles to use
Sans Serif

Colors
6b449b
5c5c5c
fdfdfd
000000

Requirements
Must have
• Logo, name, Company name, email and cell number. no Address line to be included.
Should not have
• any unrelated GFX elements, serif fonts

```html
<!DOCTYPE html>
<html lang="en">
<head>
<meta charset="utf-8">
<title>Brightwell Pictures Business Card</title>
<link rel="stylesheet" href="https://fonts.googleapis.com/css2?family=Open+Sans:wght@400;700;800&display=swap">
<style>
  :root {
    --purple: #6b449b;
    --grey: #5c5c5c;
    --white: #fdfdfd;
    --black: #000000;
    --card-black: #0a0a0a;
    --backdrop: #2b2522;
  }
  * { box-sizing: border-box; margin: 0; padding: 0; }
  html, body {
    width: 1200px;
    height: 842px;
    overflow: hidden;
    background: var(--backdrop);
    font-family: "Open Sans", Arial, sans-serif;
  }
  .canvas {
    position: relative;
    width: 1200px;
    height: 842px;
  }
  .card {
    position: absolute;
    top: 278px;
    width: 500px;
    height: 286px;
    background: linear-gradient(135deg, #141414 0%, var(--card-black) 55%, var(--black) 100%);
    overflow: hidden;
    box-shadow: 0 14px 34px rgba(0, 0, 0, 0.6);
  }

  /* Contact side */
  .card--contact { left: 80px; }
  .contact-band {
    position: absolute;
    left: 0;
    width: 100%;
    height: 13px;
    background: var(--purple);
  }
  .contact-band--top { top: 14px; }
  .contact-band--bottom { bottom: 14px; }
  .contact-details {
    position: absolute;
    top: 50px;
    left: 0;
    width: 100%;
    text-align: center;
    color: var(--white);
  }
  .person-name {
    font-size: 13px;
    font-weight: 700;
    letter-spacing: 0.3px;
    text-transform: uppercase;
  }
  .person-title {
    margin-top: 6px;
    font-size: 13px;
    font-weight: 400;
  }
  .company-name {
    margin-top: 22px;
    font-size: 13px;
    font-weight: 400;
  }
  .contact-icons {
    margin-top: 16px;
    display: flex;
    justify-content: center;
    gap: 10px;
  }
  .contact-icons svg { display: block; }
  .contact-phone,
  .contact-email {
    font-size: 13px;
    font-weight: 400;
  }
  .contact-phone { margin-top: 12px; }
  .contact-email { margin-top: 2px; }

  /* Brand side */
  .card--brand { left: 620px; }
  .accent {
    position: absolute;
    width: 34px;
    height: 40px;
    background: var(--purple);
  }
  .accent::after {
    content: "";
    position: absolute;
    top: 0;
    width: 4px;
    height: 100%;
    background: var(--white);
  }
  .accent--left { left: 0; top: 198px; }
  .accent--left::after { right: -8px; }
  .accent--right { right: 0; top: 40px; }
  .accent--right::after { left: -8px; }
  .brand-lockup {
    position: absolute;
    top: 118px;
    left: 0;
    width: 100%;
    display: flex;
    align-items: center;
    justify-content: center;
    gap: 12px;
  }
  .brand-dot {
    width: 22px;
    height: 22px;
    border-radius: 50%;
    background: var(--purple);
  }
  .brand-name {
    font-size: 34px;
    font-weight: 800;
    letter-spacing: -0.5px;
    color: var(--grey);
  }
</style>
</head>
<body>
<main class="canvas">

  <section class="card card--contact" aria-label="Contact side">
    <div class="contact-band contact-band--top"></div>
    <div class="contact-details">
      <p class="person-name">Mirela Vantasch</p>
      <p class="person-title">President/Founder</p>
      <p class="company-name">Brightwell Pictures Inc.</p>
      <div class="contact-icons">
        <svg width="10" height="14" viewBox="0 0 10 14" aria-label="Phone">
          <rect x="1" y="0.75" width="8" height="12.5" rx="1.5" fill="none" stroke="#fdfdfd" stroke-width="1.3"/>
          <line x1="4" y1="11" x2="6" y2="11" stroke="#fdfdfd" stroke-width="1.2"/>
        </svg>
        <svg width="14" height="11" viewBox="0 0 14 11" aria-label="Email">
          <rect x="0.5" y="0.5" width="13" height="10" fill="#fdfdfd"/>
          <polyline points="0.5,0.8 7,6 13.5,0.8" fill="none" stroke="#0a0a0a" stroke-width="1.2"/>
        </svg>
      </div>
      <p class="contact-phone">587 914 3362</p>
      <p class="contact-email">mirela@brightwellpix.tv</p>
    </div>
    <div class="contact-band contact-band--bottom"></div>
  </section>

  <section class="card card--brand" aria-label="Brand side">
    <div class="accent accent--right"></div>
    <div class="brand-lockup">
      <span class="brand-dot"></span>
      <span class="brand-name">Brightwell Pictures</span>
    </div>
    <div class="accent accent--left"></div>
  </section>

</main>
</body>
</html>
```